Book Cover Design 'Boundless Tide - Lessons In Inner Sovereignty'

I need to see pitches / artwork for a book cover for new book designed to start a new global spiritual movement and save humanity. The book merges science and spirituality and explains to the reader why they are an all powerful god.

```html
<!DOCTYPE html>
<html lang="en">
<head>
<meta charset="utf-8">
<title>Boundless Tide – Book Cover Spread</title>
<link rel="stylesheet" href="https://fonts.googleapis.com/css2?family=Playfair+Display:wght@900&family=Noto+Serif:wght@400&family=Oswald:wght@500&display=swap">
<style>
  :root {
    --paper: #ffffff;
    --paper-shade: #f4f4f4;
    --spine: #f1f1f1;
    --ink: #0d0d0d;
    --body-ink: #1c1c1c;
    --gold-light: #f0c46a;
    --gold-mid: #c98f34;
    --gold-dark: #8a5a1c;
    --cosmos-cyan: #35c6f2;
    --cosmos-blue: #2a5fd8;
    --cosmos-violet: #9a4fd6;
    --tree-blue: #6f9fe6;
  }
  * { margin: 0; padding: 0; box-sizing: border-box; }
  html, body { width: 1200px; height: 847px; overflow: hidden; background: var(--paper); }
  .spread { position: relative; width: 1200px; height: 847px; overflow: hidden; }

  .back-cover {
    position: absolute; left: 0; top: 0; width: 564px; height: 847px;
    background: linear-gradient(90deg, var(--paper) 0%, var(--paper) 60%, var(--paper-shade) 100%);
  }
  .spine {
    position: absolute; left: 564px; top: 0; width: 72px; height: 847px;
    background: var(--spine);
  }
  .front-cover {
    position: absolute; left: 636px; top: 0; width: 564px; height: 847px;
    background: linear-gradient(90deg, var(--paper-shade) 0%, var(--paper) 12%);
  }

  .gold-frame {
    position: absolute;
    background: linear-gradient(135deg, var(--gold-light), var(--gold-mid) 45%, var(--gold-dark) 70%, var(--gold-light));
  }
  .back-frame-edge { left: 0; top: 75px; width: 46px; height: 661px; }
  .back-frame-edge::after {
    content: ""; position: absolute; right: 0; top: 0; bottom: 0; width: 3px; background: var(--gold-dark);
  }

  .blurb {
    position: absolute; left: 110px; top: 128px; width: 380px;
    font-family: "Noto Serif", Georgia, serif; font-size: 13.6px; line-height: 17.3px;
    color: var(--body-ink); text-align: justify;
  }
  .blurb p + p { margin-top: 16px; }

  .tree-art {
    position: absolute; left: 227px; top: 567px; width: 172px; height: 150px;
    background: radial-gradient(ellipse at 50% 45%, var(--tree-blue) 0%, rgba(111,159,230,0.55) 45%, rgba(255,255,255,0) 72%);
  }

  .spine-title {
    position: absolute; left: 600px; top: 405px;
    transform: translate(-50%, -50%) rotate(-90deg);
    font-family: "Playfair Display", "Times New Roman", serif; font-weight: 900;
    font-size: 52px; line-height: 1; color: var(--ink); white-space: nowrap;
  }

  .front-frame {
    left: 728px; top: 72px; width: 379px; height: 474px;
    box-shadow: 0 10px 8px -4px rgba(0,0,0,0.25);
  }
  .front-frame::before {
    content: ""; position: absolute; inset: 10px; border: 2px solid var(--gold-dark); opacity: 0.5;
  }
  .cosmic-art {
    position: absolute; left: 50px; top: 48px; width: 278px; height: 378px;
    background:
      radial-gradient(ellipse at 78% 22%, var(--cosmos-violet) 0%, rgba(154,79,214,0) 45%),
      linear-gradient(160deg, var(--cosmos-cyan) 0%, var(--cosmos-blue) 55%, var(--cosmos-cyan) 100%);
    box-shadow: inset 0 0 0 2px rgba(138,90,28,0.6);
  }

  .cover-title {
    position: absolute; right: 93px; top: 573px; text-align: left;
    font-family: "Playfair Display", "Times New Roman", serif; font-weight: 900;
    color: var(--ink); line-height: 0.9;
  }
  .cover-title .line-one { display: block; font-size: 76px; letter-spacing: -1px; }
  .cover-title .line-two { display: block; font-size: 94px; letter-spacing: -1px; }
  .cover-subtitle {
    position: absolute; left: 731px; top: 752px; width: 376px;
    font-family: "Oswald", "Arial Narrow", sans-serif; font-weight: 500;
    font-size: 27px; line-height: 1; color: var(--ink); letter-spacing: 0.3px;
    white-space: nowrap;
  }
</style>
</head>
<body>
<main class="spread">
  <section class="back-cover">
    <div class="gold-frame back-frame-edge" role="img" aria-label="Edge of an ornate carved gold picture frame"></div>
    <div class="blurb">
      <p>Lorem ipsum dolor sit amet, consectetur adipiscing elit. Phasellus egestas suscipit porttitor. Sed a scelerisque neque. Proin dictum blandit ex, ut congue orci porta vitae. Vestibulum sed velit justo. Nam a nunc nisl. Morbi finibus vulputate lacinia. Maecenas quis congue justo. Aliquam sapien nisl, vehicula in volutpat ac, malesuada at ligula. Cras sed est id ex tempor suscipit. Morbi finibus nunc sit amet felis ornare, quis ornare dolor varius. Suspendisse at convallis ligula. Fusce elementum magna et sollicitudin pretium. Nullam non ultrices arcu. Integer tempus tempus augue et egestas.</p>
      <p>Nulla tortor leo, elementum vitae dolor ut, hendrerit hendrerit felis. Duis malesuada fermentum erat eget consequat. Integer imperdiet tempor rutrum. Donec nisl odio, semper quis dapibus dictum, convallis nec nisi. Etiam pulvinar dolor in sagittis hendrerit. Maecenas convallis hendrerit mollis. Suspendisse odio leo, feugiat ac dolor porta, faucibus euismod tellus. Nullam a ante orci. Vestibulum ante ipsum primis in faucibus orci luctus et ultrices posuere cubilia curae; Pellentesque habitant morbi tristique senectus et netus et malesuada fames ac turpis egestas.</p>
    </div>
    <div class="tree-art" role="img" aria-label="Pale blue bare tree blended with a soft double-exposure silhouette"></div>
  </section>

  <section class="spine">
  </section>
  <div class="spine-title">Boundless Tide</div>

  <section class="front-cover"></section>
  <div class="gold-frame front-frame" role="img" aria-label="Ornate carved gold picture frame">
    <div class="cosmic-art" role="img" aria-label="Glowing blue and violet cosmic scene with a DNA helix, sacred geometry lines and a branching tree"></div>
  </div>
  <h1 class="cover-title">
    <span class="line-one">Boundless</span>
    <span class="line-two">Tide</span>
  </h1>
  <p class="cover-subtitle">LESSONS IN INNER SOVEREIGNTY</p>
</main>
</body>
</html>
```